Design Banners for The Harbor Light Church

We are in need of a variety of professionally designed banners that are vibrant, fresh, and encouraging.
I have attached 2 logos, a QR code, and the current style guide.
We are moving locations to a much larger location and want it to look new and fresh.
We will need two Large (13-15ft) flag banners (2-sided) that will be out front to indicate the front entrance. These should be welcome banners and can be identical or can be complimentary.
We will need a retractable Welcome Banner (12 ft).
We will need a "Divider" Style banner that will be an intro on the road.
We will need retractable banner signs (6 feet) single-sided to be placed by children's church doors for check-in, infant to 2 years, 3 to 5 years, and 6 to 12 years.

We are looking for a wow factor, beautiful, vibrant, and inviting. The logo can be inverted. It is important that is specifically states The Harbor Light Church so that folks know it is a church.

I have also added some samples that we like...
Let me know any questions.

Target Market(s)

General Public

Industry/Entity Type

A Christian Church

Font styles to use
Other font styles liked:
• Please see included style guide.

Colors
59FF00
82FF00
B8FF75
E3FFCB
F4FFEA
F0912C
F2A743
F7CA91
FBE8D2
FDF5EE
EE7325
F08F49
F5BC92
FAE3D3
FDF4ED

Requirements
Must have
• Designs for signs and banners
Nice to have
• I have provided a copy of the current style guide including font and colors. If we could stay with oranges and greens, that would be great. But, open to fresh ideas.

```html
<!DOCTYPE html>
<html lang="en">
<head>
<meta charset="utf-8">
<title>Welcome Banner – The Harbor Light Church</title>
<link href="https://fonts.googleapis.com/css2?family=Oswald:wght@500;600&display=swap" rel="stylesheet">
<style>
  :root {
    --banner-red: #E8412F;
    --panel-lime: #DCE143;
    --text-white: #FFFFFF;
    --accent-gold: #F2A743;
    --accent-green: #7FC64E;
    --name-red: #E8412F;
  }
  html, body {
    margin: 0;
    padding: 0;
    width: 1200px;
    height: 800px;
    overflow: hidden;
  }
  .banner {
    position: relative;
    width: 1200px;
    height: 800px;
    background: var(--banner-red);
    font-family: "Oswald", sans-serif;
  }
  .welcome-message {
    position: absolute;
    left: 130px;
    top: 150px;
    margin: 0;
    font-weight: 600;
    font-size: 118px;
    line-height: 128px;
    letter-spacing: -2px;
    text-transform: uppercase;
    color: var(--text-white);
  }
  .welcome-message span { display: block; }
  .welcome-message .word-glad { color: var(--accent-gold); }
  .welcome-message .word-here { color: var(--accent-green); }
  .identity-panel {
    position: absolute;
    left: 590px;
    top: 140px;
    width: 500px;
    height: 520px;
    background: var(--panel-lime);
    display: flex;
    align-items: center;
    justify-content: center;
  }
  .church-name {
    margin: 0;
    font-weight: 500;
    font-size: 58px;
    line-height: 1.05;
    text-align: center;
    text-transform: uppercase;
    color: var(--name-red);
  }
  .church-name span { display: block; }
</style>
</head>
<body>
  <main class="banner">
    <h1 class="welcome-message">
      <span>We are</span>
      <span class="word-glad">Glad</span>
      <span>You are</span>
      <span class="word-here">Here...</span>
    </h1>
    <section class="identity-panel">
      <p class="church-name">
        <span>The</span>
        <span>Harbor Light</span>
        <span>Church</span>
      </p>
    </section>
  </main>
</body>
</html>
```